Saffron Lantern Court Business Card

I am looking for a business card desgined for my restaurant. It is an Indian restaurant, we are looking for something thats modern, yet traditional with the indian culture, we are looking for colors that match our logo. The logo is a design of the building with the name of the restaurant. for more information on the restaurant go to www.saffronlanterncourt.example

Industry/Entity Type

Indian Restaurant

Contact Information for Business Card

we are looking for somthing thats modern, yet traditional with the indian culture, we are looking for colors that match our logo. The logo is a design of the building with the name of the restaurant. for more information on the restaurant go to www.saffronlanterncourt.example

Requirements
Must have
• The logo that is attached,
• Name: Harvinder Oberoi,
• address of the restaurant: 7328 West Larkspur Rd, Phoenix, Arizona, 85213
• Phone: (602) 555-0147
• Fax: (602) 555-0193
• Restaurant Catering Banquet
• Website: www.SaffronLanternCourt.example
Nice to have
• wanted to get something that goes with the theme of the restaurant, which is traditional but also keep a very professional and modern touch

```html
<!DOCTYPE html>
<html lang="en">
<head>
<meta charset="utf-8">
<title>Saffron Lantern Court – Business Cards</title>
<link rel="stylesheet" href="https://fonts.googleapis.com/css2?family=Roboto:wght@400;700;900&display=swap">
<style>
  :root {
    --page: #f2f5f4;
    --red: #e8222b;
    --red-ink: #c8151d;
    --maroon: #6a2522;
    --maroon-ink: #531a18;
    --coral: #f4705f;
    --coral-ink: #d9473a;
    --bar-black: #1b1616;
    --bar-red: #f0331f;
    --bar-text: #ffffff;
    --back: #dedfde;
    --back-alt: #e3e4e3;
    --back-ink: #3a3a3a;
    --back-mark: #9a9a9a;
    --icon: #2d2d2d;
  }
  * { box-sizing: border-box; margin: 0; padding: 0; }
  html, body {
    width: 1200px; height: 910px; overflow: hidden;
    background: var(--page);
    font-family: "Roboto", Arial, sans-serif;
  }
  .sheet { position: relative; width: 1200px; height: 910px; }

  .card {
    position: absolute; width: 350px; height: 200px;
    overflow: hidden; border-radius: 2px;
  }

  /* fronts */
  .front { display: flex; flex-direction: column; }
  .front--red    { left: 45px;  top: 150px; background: var(--red);    --ink: var(--red-ink);    --bar: var(--bar-black); }
  .front--maroon { left: 425px; top: 150px; background: var(--maroon); --ink: var(--maroon-ink); --bar: var(--bar-red); }
  .front--coral  { left: 805px; top: 150px; background: var(--coral);  --ink: var(--coral-ink);  --bar: var(--bar-red); }

  .front__mark {
    flex: 1; display: flex; align-items: center; justify-content: center;
    text-align: center; color: var(--ink);
    font-weight: 900; font-size: 27px; line-height: 1.02;
    letter-spacing: 2px; text-transform: uppercase;
    padding-top: 6px;
  }
  .front__bar {
    height: 30px; background: var(--bar);
    display: flex; align-items: center; justify-content: space-between;
    padding: 0 14px;
  }
  .social {
    display: flex; align-items: center; gap: 5px;
    color: var(--bar-text); font-size: 7px; font-weight: 400;
  }
  .social__box {
    width: 11px; height: 11px; border: 1.2px solid var(--bar-text); border-radius: 2px;
  }

  /* backs */
  .back { background: var(--back); color: var(--back-ink); }
  .back--one { left: 235px; top: 530px; }
  .back--two { left: 615px; top: 530px; background: var(--back-alt); }

  .back__mark {
    position: absolute; left: 0; right: 0; top: 22px;
    text-align: center; color: var(--back-mark);
    font-weight: 700; font-size: 15px; letter-spacing: 2px; text-transform: uppercase;
  }
  .back__rule {
    position: absolute; left: 115px; right: 115px; top: 44px;
    height: 1px; background: var(--back-mark);
  }
  .contact {
    position: absolute; display: flex; align-items: flex-start; gap: 8px;
    font-size: 8px; font-weight: 700; line-height: 1.35;
  }
  .contact svg { flex: none; width: 16px; height: 16px; }
  .contact--name  { left: 30px;  top: 112px; font-size: 9px; }
  .contact--web   { left: 30px;  top: 148px; }
  .contact--phone { left: 200px; top: 72px; }
  .contact--place { left: 200px; top: 108px; }
</style>
</head>
<body>
<main class="sheet">

  <section class="card front front--red">
    <div class="front__mark">Saffron<br>Lantern<br>Court</div>
    <div class="front__bar">
      <span class="social"><span class="social__box"></span>@SaffronLanternCourt</span>
      <span class="social"><span class="social__box"></span>follow us @SLCourt</span>
      <span class="social"><span class="social__box"></span>follow us @slcourt</span>
    </div>
  </section>

  <section class="card front front--maroon">
    <div class="front__mark">Saffron<br>Lantern<br>Court</div>
    <div class="front__bar">
      <span class="social"><span class="social__box"></span>@SaffronLanternCourt</span>
      <span class="social"><span class="social__box"></span>follow us @SLCourt</span>
      <span class="social"><span class="social__box"></span>follow us @slcourt</span>
    </div>
  </section>

  <section class="card front front--coral">
    <div class="front__mark">Saffron<br>Lantern<br>Court</div>
    <div class="front__bar">
      <span class="social"><span class="social__box"></span>@SaffronLanternCourt</span>
      <span class="social"><span class="social__box"></span>follow us @SLCourt</span>
      <span class="social"><span class="social__box"></span>follow us @slcourt</span>
    </div>
  </section>

  <section class="card back back--one">
    <div class="back__mark">Saffron Lantern Court</div>
    <div class="back__rule"></div>
    <div class="contact contact--name">
      <svg viewBox="0 0 16 16"><circle cx="8" cy="8" r="8" fill="var(--icon)"/></svg>
      <span>Harvinder Oberoi</span>
    </div>
    <div class="contact contact--web">
      <svg viewBox="0 0 16 16"><circle cx="8" cy="8" r="7" fill="var(--icon)"/><g fill="none" stroke="#fff" stroke-width="0.9"><circle cx="8" cy="8" r="5"/><ellipse cx="8" cy="8" rx="2.2" ry="5"/><line x1="3" y1="8" x2="13" y2="8"/></g></svg>
      <span>www.SaffronLanternCourt.example</span>
    </div>
    <div class="contact contact--phone">
      <svg viewBox="0 0 16 16"><circle cx="8" cy="8" r="8" fill="var(--icon)"/><path d="M5.2 4.2l1.6-.4 1 2.2-1 .8a6 6 0 0 0 2.4 2.4l.8-1 2.2 1-.4 1.6c-3.6.4-7-3-6.6-6.6z" fill="#fff"/></svg>
      <span>(602) 555-0147<br>(602) 555-0193</span>
    </div>
    <div class="contact contact--place">
      <svg viewBox="0 0 16 16"><circle cx="8" cy="8" r="8" fill="var(--icon)"/><path d="M8 3.5a3 3 0 0 0-3 3c0 2.3 3 6 3 6s3-3.7 3-6a3 3 0 0 0-3-3z" fill="#fff"/><circle cx="8" cy="6.5" r="1.1" fill="var(--icon)"/></svg>
      <span>7328 West Larkspur Rd,<br>Phoenix,<br>Arizona, 85213</span>
    </div>
  </section>

  <section class="card back back--two">
    <div class="back__mark">Saffron Lantern Court</div>
    <div class="back__rule"></div>
    <div class="contact contact--name">
      <svg viewBox="0 0 16 16"><circle cx="8" cy="8" r="8" fill="var(--icon)"/></svg>
      <span>Harvinder Oberoi</span>
    </div>
    <div class="contact contact--web">
      <svg viewBox="0 0 16 16"><circle cx="8" cy="8" r="7" fill="var(--icon)"/><g fill="none" stroke="#fff" stroke-width="0.9"><circle cx="8" cy="8" r="5"/><ellipse cx="8" cy="8" rx="2.2" ry="5"/><line x1="3" y1="8" x2="13" y2="8"/></g></svg>
      <span>www.SaffronLanternCourt.example</span>
    </div>
    <div class="contact contact--phone">
      <svg viewBox="0 0 16 16"><circle cx="8" cy="8" r="8" fill="var(--icon)"/><path d="M5.2 4.2l1.6-.4 1 2.2-1 .8a6 6 0 0 0 2.4 2.4l.8-1 2.2 1-.4 1.6c-3.6.4-7-3-6.6-6.6z" fill="#fff"/></svg>
      <span>(602) 555-0147<br>(602) 555-0193</span>
    </div>
    <div class="contact contact--place">
      <svg viewBox="0 0 16 16"><circle cx="8" cy="8" r="8" fill="var(--icon)"/><path d="M8 3.5a3 3 0 0 0-3 3c0 2.3 3 6 3 6s3-3.7 3-6a3 3 0 0 0-3-3z" fill="#fff"/><circle cx="8" cy="6.5" r="1.1" fill="var(--icon)"/></svg>
      <span>7328 West Larkspur Rd,<br>Phoenix,<br>Arizona, 85213</span>
    </div>
  </section>

</main>
</body>
</html>
```